Membership Card Design

I need a basic membership card...it will entitle the customer to free entry to forthcoming promotions.
The business is called STARLANE PLAY and is a amusement arcade located in N Ireland.
I require .....
STARLANE PLAY MEMBER...across top of card in logo format.
Next line....this card entitles the holder free entry to forthcoming STARLANE EVENTS....
Then next line....customer name( space to write their name )
Next line.....customer mobile number ( space to write number )
On rear of card....logo/picture & STARLANE PLAY MEMBER written on back.

Industry/Entity Type

Business

Contact Information for Business Card

STARLANE PLAY
MEMBERSHIP CARD

```html
<!DOCTYPE html>
<html lang="en">
<head>
<meta charset="utf-8">
<title>Starlane Play Membership Card</title>
<link rel="stylesheet" href="https://fonts.googleapis.com/css2?family=Montserrat:wght@400;500;600;700&display=swap">
<style>
  :root {
    --backdrop: #4b4b4b;
    --white: #ffffff;
    --orange: #f28c1c;
    --silver: #d9d9dc;
    --night-top: #2a2340;
    --night-mid: #3a2a55;
    --violet: #5a2f6e;
    --magenta: #8a2f58;
    --floor-dark: #121212;
    --floor-mid: #2b2b2e;
  }
  * { box-sizing: border-box; margin: 0; padding: 0; }
  html, body { width: 1200px; height: 778px; overflow: hidden; }
  body {
    background: var(--backdrop);
    font-family: "Montserrat", sans-serif;
    position: relative;
  }
  .card {
    position: absolute;
    top: 132px;
    width: 521px;
    height: 329px;
    border-radius: 16px;
    overflow: hidden;
  }
  .card--front { left: 67px; }
  .card--back { left: 631px; }

  .card__art {
    position: absolute;
    inset: 0;
  }
  .card--front .card__art {
    background:
      linear-gradient(160deg, transparent 55%, rgba(138,47,88,0.75) 100%),
      linear-gradient(180deg, var(--night-top) 0%, var(--night-mid) 40%, var(--violet) 70%, var(--magenta) 100%);
  }
  .card--back .card__art {
    background:
      radial-gradient(ellipse at 45% 35%, #5a5a5e 0%, var(--floor-mid) 40%, var(--floor-dark) 85%);
  }

  .brand-name {
    position: absolute;
    color: var(--white);
    font-weight: 700;
    line-height: 1.05;
    text-align: center;
  }
  .card--front .brand-name {
    left: 38px;
    top: 48px;
    width: 136px;
    font-size: 20px;
  }
  .card--back .brand-name {
    left: 0;
    width: 100%;
    top: 100px;
    font-size: 40px;
    letter-spacing: 1px;
  }

  .title {
    position: absolute;
    left: 192px;
    top: 42px;
    font-size: 37px;
    font-weight: 600;
    color: var(--white);
    letter-spacing: 1px;
  }
  .events {
    position: absolute;
    left: 194px;
    top: 90px;
    font-size: 17px;
    font-weight: 500;
    color: var(--orange);
    letter-spacing: 0.5px;
  }
  .events b { font-weight: 700; }

  .holder-name {
    position: absolute;
    left: 46px;
    top: 237px;
    font-size: 29px;
    font-weight: 600;
    color: var(--white);
    letter-spacing: 0.5px;
  }
  .holder-number {
    position: absolute;
    left: 46px;
    top: 275px;
    font-size: 24px;
    font-weight: 600;
    color: var(--orange);
    letter-spacing: 0.5px;
  }
  .validity {
    position: absolute;
    left: 286px;
    top: 284px;
    font-size: 11px;
    font-weight: 700;
    color: #e8e8ee;
  }
  .validity span { color: var(--orange); }

  .back-title {
    position: absolute;
    left: 0;
    width: 100%;
    top: 210px;
    text-align: center;
    font-size: 56px;
    font-weight: 500;
    color: var(--silver);
    letter-spacing: 2px;
  }
</style>
</head>
<body>
  <section class="card card--front" aria-label="Membership card front">
    <div class="card__art" role="img" aria-label="Starry night sky over faceted low-poly purple and magenta mountains"></div>
    <div class="brand-name">STARLANE<br>PLAY</div>
    <h1 class="title">MEMBER</h1>
    <p class="events"><b>STARLANE</b> EVENTS</p>
    <p class="holder-name">MEMBERSHIP NAME</p>
    <p class="holder-number">111-222-333-444</p>
    <p class="validity">VALID THRU: <span>08/14</span></p>
  </section>

  <section class="card card--back" aria-label="Membership card back">
    <div class="card__art" role="img" aria-label="Dimly lit arcade floor with roulette gaming machines under a columned club sign"></div>
    <div class="brand-name">STARLANE PLAY</div>
    <p class="back-title">MEMBER</p>
  </section>
</body>
</html>
```